Flyer for tutoring

The text should be presented in an engaging way to attract potential customers.
Colorfully designed
Around the edge, various objects related to school and the subjects (see text) should be visible.

```html
<!DOCTYPE html>
<html lang="de">
<head>
<meta charset="utf-8">
<title>Nachhilfe Flyer</title>
<link rel="stylesheet" href="https://fonts.googleapis.com/css2?family=Barlow:wght@400;700;800&family=Open+Sans:wght@400;600&display=swap">
<style>
  :root {
    --yellow-light: #fdf17a;
    --yellow: #f5e423;
    --white: #ffffff;
    --ink: #111111;
    --grey-text: #555555;
    --shadow-grey: #58585a;
    --orange: #e55521;
    --blue: #3a62b0;
    --rule: #cfcfcf;
  }
  * { box-sizing: border-box; margin: 0; padding: 0; }
  html, body { width: 801px; height: 1200px; overflow: hidden; background: #9a9a9a; }
  .flyer {
    position: relative; width: 801px; height: 1200px; overflow: hidden;
    background: var(--white); font-family: "Open Sans", sans-serif; color: var(--ink);
  }
  .backdrop { position: absolute; left: 0; top: 0; }
  .intro {
    position: absolute; left: 55px; top: 52px;
    font-family: "Barlow", sans-serif; color: var(--grey-text);
    font-size: 31px; line-height: 32px; font-weight: 400;
  }
  .headline {
    position: absolute; left: 53px; top: 132px;
    font-family: "Barlow", sans-serif; line-height: 58px;
  }
  .headline .accent { display: block; color: var(--orange); font-size: 60px; font-weight: 400; }
  .headline .main { display: block; color: var(--ink); font-size: 60px; font-weight: 800; letter-spacing: 0.5px; }
  .invite {
    position: absolute; left: 55px; top: 382px;
    font-family: "Barlow", sans-serif; font-weight: 700; font-size: 29px; line-height: 30px;
  }
  .invite svg { vertical-align: -8px; margin-left: 4px; }
  .details {
    position: absolute; left: 55px; top: 480px; width: 420px;
    font-size: 19px; line-height: 24px; color: #1d1d1d;
  }
  .details p + p { margin-top: 24px; }
  .photo {
    position: absolute; left: 461px; top: 413px; width: 340px; height: 345px;
    background: radial-gradient(ellipse at 60% 60%, #e8473a 0%, #f0a33a 40%, rgba(245,228,35,0) 75%);
  }
  .promise {
    position: absolute; left: 55px; top: 757px; width: 691px; height: 110px;
    background: var(--blue); border-radius: 6px; padding: 4px;
    box-shadow: 0 14px 12px -10px rgba(0,0,0,0.35);
  }
  .promise-inner {
    height: 100%; border: 2px dashed rgba(255,255,255,0.85); border-radius: 4px;
    display: flex; align-items: center; justify-content: center; text-align: center;
    font-family: "Barlow", sans-serif; font-weight: 700; font-size: 37px; line-height: 38px; color: var(--white);
  }
  .about-badge {
    position: absolute; left: 57px; top: 896px; width: 98px; height: 98px; border-radius: 50%;
    background: var(--ink); color: var(--white);
    display: flex; align-items: center; justify-content: center; text-align: center;
    font-family: "Barlow", sans-serif; font-weight: 700; font-size: 23px; line-height: 21px;
  }
  .about-text {
    position: absolute; left: 183px; top: 897px; width: 580px;
    font-size: 19px; line-height: 24px; color: #1d1d1d;
  }
  .divider { position: absolute; left: 55px; top: 1026px; width: 691px; height: 1px; background: var(--rule); }
  .contact { position: absolute; top: 1058px; display: flex; align-items: flex-start; gap: 14px; }
  .contact.phone { left: 55px; }
  .contact.mail { left: 417px; }
  .contact-icon { flex: none; margin-top: 4px; }
  .phone-number { font-family: "Barlow", sans-serif; font-weight: 800; font-size: 33px; line-height: 36px; }
  .phone-note { font-size: 12px; color: var(--grey-text); letter-spacing: -0.3px; }
  .mail-address { font-size: 23px; line-height: 40px; color: #1d1d1d; }
  .closing {
    position: absolute; left: 0; bottom: 0; width: 801px; height: 77px; background: var(--orange);
    display: flex; align-items: center; justify-content: center; gap: 12px;
    color: var(--white); font-size: 24px;
  }
</style>
</head>
<body>
<main class="flyer">
  <svg class="backdrop" width="801" height="1200" viewBox="0 0 801 1200" aria-hidden="true">
    <defs>
      <linearGradient id="sunny" x1="1" y1="0" x2="0" y2="1">
        <stop offset="0" stop-color="#f0de3a"/>
        <stop offset="0.45" stop-color="#fbee6a"/>
        <stop offset="1" stop-color="#f5e31a"/>
      </linearGradient>
    </defs>
    <rect x="0" y="0" width="801" height="797" fill="url(#sunny)"/>
    <path d="M0 342 H417 L617 490 V506 L405 362 H0 Z" fill="var(--shadow-grey)"/>
    <path d="M617 342 H722 Q744 342 744 322 V340 Q744 362 722 362 H617 Z" fill="var(--shadow-grey)"/>
    <path d="M0 0 H744 V322 Q744 342 724 342 H617 V490 L417 342 H0 Z" fill="var(--white)"/>
  </svg>

  <p class="intro">Möchtest du dich gerne in der<br>Schule verbessern und suchst eine</p>
  <h1 class="headline">
    <span class="accent">Professionelle</span>
    <span class="main">NACHHILFELEHRERIN /</span>
    <span class="main">LERNCOACH?</span>
  </h1>

  <h2 class="invite">Dann lass es uns doch<br>mal versuchen!<svg width="32" height="32" viewBox="0 0 32 32"><circle cx="16" cy="16" r="14" fill="none" stroke="#f4c542" stroke-width="2"/><circle cx="12" cy="13" r="1.6" fill="#f4c542"/><circle cx="20" cy="13" r="1.6" fill="#f4c542"/><path d="M9 18 Q16 26 23 18" fill="none" stroke="#f4c542" stroke-width="2"/></svg></h2>

  <div class="details">
    <p>Die erste Lektion – die Kennenlernlektion – dauert ca. 30 Minuten. Sie ist kostenlos. Denn wir müssen ja sicher gehen, dass wir uns verstehen und leiden können. Bei unserem ersten Treffen legen wir auch fest, woran wir arbeiten werden und wann die Nachhilfe in deine Agenda passt.</p>
    <p>Wenn der erste Eindruck stimmt, dann legen wir los, und bald schon werden</p>
  </div>

  <div class="photo" role="img" aria-label="Foto: fröhliches Kind im roten T-Shirt mit einem Stapel Bücher, umgeben von bunten Schul-Doodles"></div>

  <div class="promise"><div class="promise-inner">DEINE MOTIVATION UND<br>DEINE NOTEN BESSER UND BESSER!</div></div>

  <div class="about-badge">Zu<br>meiner<br>Person</div>
  <p class="about-text">Ich wohne hier in der Siedlung Lindenhof und bin ausgebildete und sehr erfahrene Sekundar- und Primarlehrerin in den Fächern Deutsch, Französisch, Englisch und Geschichte. (Auf Wunsch auch Mathe-Nachhilfe möglich.)</p>

  <div class="divider"></div>

  <div class="contact phone">
    <svg class="contact-icon" width="26" height="26" viewBox="0 0 26 26" aria-hidden="true"><circle cx="13" cy="13" r="13" fill="var(--orange)"/><path d="M9 7 L11 10 L10 12 Q11 15 14 16 L16 15 L19 17 L18 19 Q12 20 8 13 Q7 9 9 7 Z" fill="#fff"/></svg>
    <div>
      <div class="phone-number">079 512 48 17</div>
      <div class="phone-note">(nachmittags fast immer erreichbar)</div>
    </div>
  </div>

  <div class="contact mail">
    <svg class="contact-icon" width="26" height="26" viewBox="0 0 26 26" aria-hidden="true"><circle cx="13" cy="13" r="13" fill="var(--orange)"/><rect x="6.5" y="8.5" width="13" height="9" fill="none" stroke="#fff" stroke-width="1.5"/><path d="M6.5 8.5 L13 14 L19.5 8.5 M6.5 17.5 L11 13 M19.5 17.5 L15 13" fill="none" stroke="#fff" stroke-width="1.3"/></svg>
    <div class="mail-address">lina.vogt@lernpost.ch</div>
  </div>

  <footer class="closing">
    <span>Ich freue mich auf deine Kontaktaufnahme! Bis bald!</span>
    <svg width="20" height="20" viewBox="0 0 20 20" aria-hidden="true"><circle cx="10" cy="10" r="8.5" fill="none" stroke="#fff" stroke-width="1.5"/><circle cx="7.5" cy="8" r="1" fill="#fff"/><circle cx="12.5" cy="8" r="1" fill="#fff"/><path d="M6 11.5 Q10 16 14 11.5" fill="none" stroke="#fff" stroke-width="1.5"/></svg>
  </footer>
</main>
</body>
</html>
```